Consulting company needs Business Cards - rough concept provided

I'm looking for someone to take our business card idea and make is slick and polished - to communicate our high-end, sophisticated, serious consulting business. We have a rough layout we did in-house. We are open to ideas on repo-ing elements, adjusting sizes, typefaces etc... within the general concept we've already come up with. We want it to be super-clean and sophisticated. We want to keep the white backgrounds, and blue brand colors. Our goal is to print with painted blue edges on thick cardstock. Thank you!!

```html
<!DOCTYPE html>
<html lang="en">
<head>
<meta charset="utf-8">
<title>KEENSTRATA Business Card</title>
<link href="https://fonts.googleapis.com/css2?family=Poppins:wght@400;500;600;700&display=swap" rel="stylesheet">
<style>
  :root {
    --brand-blue: #0085ca;
    --pattern-blue: #0a8fd3;
    --stage-grey: #717070;
    --card-white: #ffffff;
    --divider-grey: #a8a8a8;
    --label-white: #ffffff;
  }
  * { margin: 0; padding: 0; box-sizing: border-box; }
  html, body {
    width: 965px; height: 1200px; overflow: hidden;
    background: var(--stage-grey);
    font-family: "Poppins", sans-serif;
  }
  .stage { position: relative; width: 965px; height: 1200px; }
  .side-label {
    position: absolute; left: 114px;
    font-family: Arial, Helvetica, sans-serif;
    font-size: 16px; color: var(--label-white); letter-spacing: 0.2px;
  }
  .side-label--front { top: 72px; }
  .side-label--back { top: 604px; }

  .card {
    position: absolute;
    box-shadow: 14px 22px 28px rgba(0,0,0,0.35);
  }
  .card--front {
    left: 115px; top: 111px; width: 745px; height: 426px;
    background: var(--card-white);
    border: 2px solid var(--brand-blue);
  }
  .card--back {
    left: 119px; top: 646px; width: 748px; height: 428px;
    background: var(--brand-blue);
    overflow: hidden;
  }

  .wordmark { position: absolute; display: block; }
  .wordmark text { font-family: "Poppins", sans-serif; font-weight: 600; }
  .card--front .wordmark { left: 33px; top: 40px; }
  .card--front .wordmark text { fill: var(--brand-blue); }

  .person { position: absolute; left: 43px; top: 243px; color: var(--brand-blue); }
  .person__name { font-size: 39px; font-weight: 600; line-height: 1.05; letter-spacing: -0.5px; }
  .person__title { font-size: 25px; font-weight: 400; line-height: 1.05; margin-left: 2px; }

  .divider {
    position: absolute; left: 385px; top: 187px;
    width: 3px; height: 185px; background: var(--divider-grey);
  }

  .contact { position: absolute; left: 412px; color: var(--brand-blue); font-weight: 600; font-size: 18.5px; line-height: 23px; }
  .contact__icon { position: absolute; left: 0; }
  .contact__text { position: absolute; left: 35px; white-space: nowrap; }
  .contact--address { top: 207px; }
  .contact--address .contact__icon { top: 2px; }
  .contact--phone { top: 272px; }
  .contact--phone .contact__icon { top: 0; }
  .contact--phone .contact__text { left: 32px; }
  .contact--email { top: 330px; }
  .contact--email .contact__icon { top: 3px; }

  .back-pattern {
    position: absolute; inset: 0;
    background: linear-gradient(180deg, var(--pattern-blue), var(--brand-blue));
  }
  .card--back .wordmark { left: 74px; top: 179px; }
  .card--back .wordmark text { fill: var(--card-white); }
</style>
</head>
<body>
<main class="stage">
  <p class="side-label side-label--front">FRONT</p>

  <section class="card card--front" aria-label="Business card front">
    <svg class="wordmark" width="676" height="92" viewBox="0 0 676 92" aria-label="KEENSTRATA">
      <text x="0" y="89" font-size="124" textLength="676" lengthAdjust="spacingAndGlyphs">KEENSTRATA</text>
    </svg>

    <div class="person">
      <p class="person__name">Dana Whitfield</p>
      <p class="person__title">Brand Consultant</p>
    </div>

    <div class="divider"></div>

    <div class="contact contact--address">
      <svg class="contact__icon" width="26" height="34" viewBox="0 0 26 34" aria-hidden="true">
        <path d="M13 2C7 2 2.5 6.5 2.5 12.3 2.5 20 13 32 13 32s10.5-12 10.5-19.7C23.5 6.5 19 2 13 2z" fill="var(--brand-blue)"/>
        <circle cx="13" cy="12.3" r="5" fill="var(--card-white)"/>
      </svg>
      <p class="contact__text">4820 Harbor Lane, Ste 210<br>Lakeview, CA 90412</p>
    </div>

    <div class="contact contact--phone">
      <svg class="contact__icon" width="24" height="26" viewBox="0 0 24 26" aria-hidden="true">
        <path d="M5 1.5l4 .5 2 6-3 2.5c1.3 3.5 3.7 6.2 7 8l2.6-2.8 5.9 2.2.3 4.3c-.2 1.6-1.7 2.8-3.4 2.8C10 24 .5 14 1 4.8 1.1 3 2.8 1.6 5 1.5z" fill="var(--brand-blue)"/>
      </svg>
      <p class="contact__text">(555) 014 2763</p>
    </div>

    <div class="contact contact--email">
      <svg class="contact__icon" width="30" height="22" viewBox="0 0 30 22" aria-hidden="true">
        <rect x="2" y="2" width="26" height="18" rx="4" fill="none" stroke="var(--brand-blue)" stroke-width="3"/>
        <path d="M4 5l11 8 11-8" fill="none" stroke="var(--brand-blue)" stroke-width="3" stroke-linejoin="round"/>
      </svg>
      <p class="contact__text">dana@keenstrata.com</p>
    </div>
  </section>

  <p class="side-label side-label--back">BACK</p>

  <section class="card card--back" aria-label="Business card back">
    <div class="back-pattern" role="img" aria-label="Faint repeated outline wordmark pattern in lighter blue"></div>
    <svg class="wordmark" width="590" height="78" viewBox="0 0 590 78" aria-label="KEENSTRATA">
      <text x="0" y="76" font-size="106" textLength="590" lengthAdjust="spacingAndGlyphs">KEENSTRATA</text>
    </svg>
  </section>
</main>
</body>
</html>
```